2020-23 Strategic Plan - Graphic Design Work

We would would like to have our strategic plan designed. It should be two pages.

- I am looking for suggestions on ways to lay this out. I don’t like this boxy layout. It was great for the committee as we went through multiple versions, but I’d prefer the final not follow this boxy format

- I’ve included a few images we own (feel free to use any or none of them). Also attached our logo.

- Have a look at our new website to see our new branding look and feel (launching next week) https://thevorlex.plinthweb.com/

- I've included a copy of our logo.

Target Market(s)

Membership

Other font styles liked:
• Lato

Requirements
Must have
• Excellent layout. Easy to ready. Consistent with branding.

```html
<!DOCTYPE html>
<html lang="en">
<head>
<meta charset="utf-8">
<title>Vorlex Institute of Assessors – 2020-2023 Strategic Plan</title>
<link href="https://fonts.googleapis.com/css2?family=Raleway:ital,wght@0,300;0,400;0,500;0,800;0,900;1,500&display=swap" rel="stylesheet">
<style>
  :root {
    --green-dark: #0c4528;
    --green-mid: #4b8d3c;
    --green-panel: rgba(86, 150, 72, 0.93);
    --green-stripe: #4f9a43;
    --red: #e11e26;
    --grey-heading: #5c5c5c;
    --text: #222;
    --white: #fff;
  }
  * { margin: 0; padding: 0; box-sizing: border-box; }
  html, body { width: 959px; height: 1200px; overflow: hidden; background: var(--white); }
  body { font-family: "Raleway", sans-serif; color: var(--text); }
  .page { position: relative; width: 959px; height: 1200px; background: var(--white); }

  .brand { position: absolute; left: 72px; top: 70px; display: flex; align-items: center; gap: 14px; }
  .brand-mark { width: 40px; height: 40px; background: var(--green-mid); }
  .brand-name { font-size: 26px; font-weight: 800; color: var(--green-dark); line-height: 1.05; }

  .site-url { position: absolute; left: 624px; top: 84px; font-size: 24px; font-weight: 500; color: var(--green-dark); letter-spacing: 0.3px; }

  .hero-photo {
    position: absolute; left: 0; top: 200px; width: 959px; height: 465px;
    background: linear-gradient(160deg, #2d3a6a 0%, #7a6a9c 30%, #c79aa8 45%, #6a5f8e 65%, #23304f 100%);
  }
  .plan-years { position: absolute; left: 68px; top: 362px; font-size: 72px; font-weight: 400; color: var(--white); letter-spacing: 1px; line-height: 1; }
  .plan-title { position: absolute; left: 66px; top: 440px; font-size: 84px; font-weight: 900; color: var(--white); line-height: 1; letter-spacing: -0.5px; }

  .accent-bar { position: absolute; left: 70px; top: 526px; width: 118px; height: 281px; background: var(--red); }
  .intro-panel { position: absolute; left: 206px; top: 526px; width: 685px; height: 281px; background: var(--green-panel); padding: 16px 20px 0 26px; }
  .intro-panel p { font-size: 18.2px; font-weight: 500; font-style: italic; color: var(--white); line-height: 23px; }
  .intro-panel p + p { margin-top: 16px; }

  .pillar { position: absolute; top: 838px; width: 250px; }
  .pillar h2 { font-size: 50px; font-weight: 800; line-height: 1; margin-bottom: 16px; letter-spacing: -0.5px; }
  .pillar p { font-size: 14.2px; font-weight: 400; line-height: 17.2px; }
  .pillar--vision { left: 66px; }
  .pillar--vision h2 { color: var(--green-mid); }
  .pillar--mission { left: 355px; }
  .pillar--mission h2 { color: var(--green-dark); }
  .pillar--values { left: 640px; }
  .pillar--values h2 { color: var(--grey-heading); }

  .footer-band { position: absolute; left: 0; top: 1122px; width: 959px; height: 78px; }
</style>
</head>
<body>
<main class="page">
  <header>
    <div class="brand">
      <span class="brand-mark"></span>
      <span class="brand-name">Vorlex Institute<br>of Assessors</span>
    </div>
    <div class="site-url">www.thevorlex.ca</div>
  </header>

  <section class="hero">
    <div class="hero-photo" role="img" aria-label="Upward view of glass skyscrapers against a streaked violet and pink sky"></div>
    <div class="plan-years">2020-2023</div>
    <h1 class="plan-title">STRAGETIC PLAN</h1>
    <div class="accent-bar"></div>
    <div class="intro-panel">
      <p>Incorporated in May 1957, the Vorlex Institute of Assessors is dedicated to advancing the interests, education and professional competence of its members. Our members are highly qualified and widely recognized as the leading professionals in the property assessment industry.</p>
      <p>With over 1,250 members, the VIA is Canada's largest association of property assessment and taxation professionals. Our diverse membership is comprised of individuals from the private and public sectors practicing in the fields of assessment, consultancy, appraisal, taxation and law.</p>
    </div>
  </section>

  <section class="pillars">
    <article class="pillar pillar--vision">
      <h2>Vision</h2>
      <p>To be the industry leader in education, ethical standards, and professional accreditation in the field of property assessment in Canada.</p>
    </article>
    <article class="pillar pillar--mission">
      <h2>Mission</h2>
      <p>To provide specialized education through a comprehensive approach to training which embraces all available technologies. To promote professional development and to ensure our members are recognized as experts in the field of property assessment and related functions.</p>
    </article>
    <article class="pillar pillar--values">
      <h2>Values</h2>
      <p>The Vorlex Institute of Assessors and its members value professionalism, inclusivity, diversity, integrity, ethics, accountability, and expertise. The VIA is committed to serving all members and stakeholders with competence and respect, rejecting all forms of prejudice and discrimination.</p>
    </article>
  </section>

  <svg class="footer-band" viewBox="0 0 959 78" aria-hidden="true">
    <polygon points="0,0 352,0 396,32 959,32 959,78 0,78" fill="var(--green-dark)"/>
    <polygon points="366,14 959,14 959,22 377,22" fill="var(--green-stripe)"/>
  </svg>
</main>
</body>
</html>
```